Eco friendly Swedish beauty products sold in aluminum bottles - label design needed

We need help in designing a series of stick on labels for 80 ml (2.7 fl. oz.) aluminum bottles containing beauty products such as soaps, shampoo etc. The diameter of the bottle is 36 mm and the body of the bottles measures approx. 106 mm.
It is important for us that the label has a simplistic and clean feel with few colors (and the right ones!) and that the label helps amplify this product being both better and a more sustainable alternative to many of our plastic bottle competitors. The design and label should communicate the feel of an Eco-friendly, sustainable and modern brand of high quality - and with a Swedish concept.
We are using Montserrat font in our materials. Find attached information of preferred colors, the bottles and one example of our logotype. I am also available on e-mail should further information be needed.

Looking forward and very excited to receive your suggestions.
Note that we are expecting to start selling a series of approximately 10 different products where I will need one "master design" and then only smaller changes for each of the different products.

Target Market(s)

People whom are aware and not only look at price tag. Private and commercial market.

Industry/Entity Type

Beauty

Font styles to use
Other font styles liked:
• Montserrat

Requirements
Must have
• It must give the feel of being both better and a more sustainable alternative to many of our plastic bottle competitors.
Nice to have
• Simplistic. Clean. Clear.
Should not have
• Wrong colors, too complex designs.

```html
<!DOCTYPE html>
<html lang="en">
<head>
<meta charset="utf-8">
<title>Lindvik – Hair Shampoo label series</title>
<link href="https://fonts.googleapis.com/css2?family=Antonio:wght@100;200&family=Montserrat:wght@300;400&display=swap" rel="stylesheet">
<style>
  :root {
    --paper: #ffffff;
    --ink: #111111;
    --gold: #d4b07e;
    --silver-dark: #9a9a9a;
    --silver-mid: #c9c9c9;
    --silver-light: #f1f1f1;
    --cap-dark: #7a5a2c;
    --cap-light: #e8c896;
  }
  html, body {
    margin: 0;
    padding: 0;
    width: 1200px;
    height: 1200px;
    overflow: hidden;
    background: var(--paper);
  }
  .board {
    display: block;
    width: 1200px;
    height: 1200px;
  }
  .product-line {
    font-family: "Antonio", "Arial Narrow", sans-serif;
    font-weight: 100;
    font-size: 40px;
  }
  .brand-name {
    font-family: "Montserrat", Arial, sans-serif;
    font-weight: 300;
    font-size: 62px;
  }
  .volume {
    font-family: "Montserrat", Arial, sans-serif;
    font-weight: 300;
    font-size: 22px;
  }
  .label-frame {
    fill: none;
    stroke-width: 6;
    stroke-linejoin: miter;
  }
  .label--ink { fill: var(--ink); }
  .label--ink .label-frame { stroke: var(--ink); }
  .label--gold { fill: var(--gold); }
  .label--gold .label-frame { stroke: var(--gold); }
</style>
</head>
<body>
<svg class="board" viewBox="0 0 1476 1476" xmlns="http://www.w3.org/2000/svg">
  <defs>
    <linearGradient id="bottle-metal" x1="0" y1="0" x2="1" y2="0">
      <stop offset="0" stop-color="var(--silver-dark)"/>
      <stop offset="0.3" stop-color="var(--silver-light)"/>
      <stop offset="0.6" stop-color="var(--silver-mid)"/>
      <stop offset="1" stop-color="var(--silver-dark)"/>
    </linearGradient>
    <linearGradient id="cap-metal" x1="0" y1="0" x2="1" y2="0">
      <stop offset="0" stop-color="var(--cap-dark)"/>
      <stop offset="0.35" stop-color="var(--cap-light)"/>
      <stop offset="1" stop-color="var(--cap-dark)"/>
    </linearGradient>

    <g id="label-artwork">
      <text class="product-line" x="148" y="445" textLength="304" lengthAdjust="spacing">HAIR SHAMPOO</text>
      <path class="label-frame" d="M203 1250 V468 H408 V1135 A133 133 0 0 1 275 1268 A120 120 0 0 1 203 1250 Z"/>
      <text class="brand-name" transform="translate(298 505) rotate(90)" textLength="440" lengthAdjust="spacing">LINDVIK</text>
      <text class="volume" transform="translate(188 1238) rotate(-90)">80 ml</text>
    </g>
  </defs>

  <g class="label label--ink">
    <use href="#label-artwork"/>
  </g>

  <g class="label label--gold">
    <use href="#label-artwork" transform="translate(390 0)"/>
  </g>

  <g class="bottle" role="img" aria-label="Brushed aluminium 80 ml bottle with a gold metal cap">
    <rect x="1022" y="108" width="245" height="136" fill="url(#cap-metal)"/>
    <path d="M1030 244 H1260 C1262 300 1345 320 1348 400 V1312 H944 V400 C947 320 1028 300 1030 244 Z" fill="url(#bottle-metal)"/>
  </g>

  <g class="label label--gold">
    <use href="#label-artwork" transform="translate(840 0)"/>
  </g>
</svg>
</body>
</html>
```